Structural Engineering Company needs ad for magazine

We are an engineering office for structural engineering in the entertainment industry. Our focus are concert stages, festival structures, grand stands and exhibition booths. Our customers are mainly from Europe, we realize the projects worldwide. Typical customers are designer, architects, stage builders, exhibition builder and technical service provider. We are creating structural analyses, technical consulting, technical drawings and risk assessment. We are working on mid size and major events.
Some technical notes:
- CMYK profile needed, minimum 300 dpi for raster graphic
- Our primary color is Petrol. Favourite is petrol, coral and grey (black). Please use palette shown below.
- Our font in documents is Myriad. Regular at 10 pt for text and Light at 16-24pt for titles.
- The format for the ad is 61 x 127 mm (portrait) or 185 x 46 mm (landscape). Which one is up to you.
To the content:
- For contact details we just want to provide our web address "belsokar.de" and/or our e-mail "info@belsokar.de"
- Attached are some Logo files and photos.
- The ad do not advertise a specific product. It is more a general advertisement for the company.
- The language for the ad should be German. Below are keywords in English and corresponding German translation. You do not need to place all Keywords, it is just a brainstorming list to help you. You are also welcome to use other text. We will help with translation, if necessary.
- we like discussing ideas to get better results, so also if you have questions, please ask.
- If you need information that we haven't thought of yet, please ask.
Our slogan (also in Germany): event meets engineering
Service Keywords EN / DE
- Structural Analysis / Statische Berechnungen
- Risk Assessment / Risikobewertungen
- Consulting & Design / Beratung & Konstruktion
Technical Keywords EN / DE
- Stage machinery / Bühnentechnik
- Scaffolding / Gerüstbau
- Exhibition Booths / Messebauten
- Tents / Zelte
- Temporary Structures / Fliegende Bauten
- Truss / Traversen
- Stages / Bühnen
- Grand Stands / Tribünen
- Leightweight Construction / Leichtbau
- Steel Construction / Stahlbau
- Amusement Rides / Fahrgeschäfte
Look and feel
Each slider illustrates characteristics of the customer's brand and the style your logo design should communicate.

```html
<!DOCTYPE html>
<html lang="de">
<head>
<meta charset="utf-8">
<title>Belsokar Engineering – Anzeige</title>
<link href="https://fonts.googleapis.com/css2?family=Source+Sans+3:wght@300;400&display=swap" rel="stylesheet">
<style>
  :root {
    --stage: #e6e7e9;
    --paper: #ffffff;
    --ink: #2b2b2b;
    --ink-soft: #3c3c3c;
    --petrol: #26bcd3;
    --coral: #e8636f;
    --amber: #d9a24c;
    --rule: #e3e3e3;
  }
  * { margin: 0; padding: 0; box-sizing: border-box; }
  html, body { width: 716px; height: 1200px; overflow: hidden; }
  body {
    background: var(--stage);
    font-family: "Source Sans 3", "Myriad Pro", sans-serif;
    position: relative;
  }
  .ad {
    position: absolute;
    left: 118px; top: 100px;
    width: 480px; height: 1000px;
    background: var(--paper);
  }
  .ad-header { position: absolute; left: 0; top: 0; width: 480px; height: 166px; }
  .brand {
    position: absolute; left: 0; top: 0; width: 255px; height: 166px;
    display: flex; flex-direction: column; align-items: center; justify-content: center;
    color: var(--ink); font-weight: 400; text-transform: uppercase;
  }
  .brand-name { font-size: 30px; letter-spacing: 5px; line-height: 1; }
  .brand-sub { font-size: 10px; letter-spacing: 3px; margin-top: 6px; }
  .header-divider {
    position: absolute; left: 255px; top: 35px; width: 1px; height: 102px;
    background: var(--rule);
  }
  .slogan {
    position: absolute; left: 288px; top: 50px;
    font-size: 25px; font-weight: 300; line-height: 33px; color: var(--ink);
  }
  .slogan strong { color: var(--petrol); font-weight: 400; }

  .service {
    position: absolute; left: 0; width: 480px; height: 180px;
    overflow: hidden;
  }
  .service-photo { position: absolute; inset: 0; }
  .service--analysis { top: 166px; }
  .service--analysis .service-photo {
    background: linear-gradient(180deg, #2a2f35 0%, #4a5661 35%, #2f7f97 65%, #1f3e5f 85%, #1a1d22 100%);
  }
  .service--risk { top: 360px; }
  .service--risk .service-photo {
    background: radial-gradient(ellipse at 62% 45%, #b9bcbe 0%, #8d9093 30%, #3a3b3c 60%, #0b0b0b 85%);
  }
  .service--design { top: 552px; }
  .service--design .service-photo {
    background: linear-gradient(160deg, #3b3a44 0%, #4d2a36 35%, #8a3a4c 60%, #c85a6c 78%, #2a1a1e 100%);
  }
  .service-title {
    position: absolute; left: 22px;
    padding-left: 14px;
    border-left: 3px solid var(--petrol);
    color: #fff; font-size: 27px; font-weight: 400; line-height: 35px;
    text-shadow: 0 1px 3px rgba(0,0,0,.35);
  }
  .service--analysis .service-title { top: 52px; }
  .service--risk .service-title { top: 72px; border-color: var(--coral); }
  .service--design .service-title { top: 52px; border-color: var(--amber); }

  .keywords {
    position: absolute; left: 0; top: 767px; width: 480px;
    text-align: center; color: var(--ink-soft);
    font-size: 20px; font-weight: 300; line-height: 36px; letter-spacing: -0.2px;
  }
  .contact-bar {
    position: absolute; left: 0; top: 911px; width: 480px; height: 89px;
    background: var(--petrol); color: #fff;
  }
  .contact {
    position: absolute; top: 30px; display: flex; align-items: center;
    font-size: 21px; font-weight: 300; line-height: 28px;
  }
  .contact svg { margin-right: 11px; }
  .contact--mail { left: 36px; }
  .contact--web { left: 288px; }
</style>
</head>
<body>
  <main class="ad">
    <header class="ad-header">
      <div class="brand">
        <span class="brand-name">Belsokar</span>
        <span class="brand-sub">Engineering</span>
      </div>
      <div class="header-divider"></div>
      <p class="slogan">event <strong>meets</strong><br>engineering</p>
    </header>

    <section class="service service--analysis">
      <div class="service-photo" role="img" aria-label="Stadion mit Bühnengerüst aus Traversen und einem gelben Mobilkran im Aufbau"></div>
      <h2 class="service-title">Statische<br>Berechnungen</h2>
    </section>

    <section class="service service--risk">
      <div class="service-photo" role="img" aria-label="Nahaufnahme eines Gerüstknotens mit sternförmig angeschlossenen Stahlrohren"></div>
      <h2 class="service-title">Risikobewertungen</h2>
    </section>

    <section class="service service--design">
      <div class="service-photo" role="img" aria-label="Konzertbühne mit LED-Wänden und roter Beleuchtung vor Publikum"></div>
      <h2 class="service-title">Beratung &amp;<br>Konstruktion</h2>
    </section>

    <p class="keywords">
      Bühnentechnik • Gerüstbau • Messebauten •<br>
      Zelte • Fliegende Bauten • Traversen • Bühnen •<br>
      Tribünen • Leichtbau • Stahlbau • Fahrgeschäfte
    </p>

    <footer class="contact-bar">
      <span class="contact contact--mail">
        <svg width="21" height="16" viewBox="0 0 21 16" fill="none" stroke="#fff" stroke-width="1.6">
          <rect x="1" y="1" width="19" height="14" rx="2"/>
          <path d="M1.5 2.5 L10.5 9 L19.5 2.5"/>
        </svg>
        info@belsokar.de
      </span>
      <span class="contact contact--web">
        <svg width="21" height="21" viewBox="0 0 21 21" fill="none" stroke="#fff" stroke-width="1.4">
          <circle cx="10.5" cy="10.5" r="9.5"/>
          <ellipse cx="10.5" cy="10.5" rx="4.2" ry="9.5"/>
          <path d="M1 10.5 H20 M2.6 5.5 H18.4 M2.6 15.5 H18.4"/>
        </svg>
        belsokar.de
      </span>
    </footer>
  </main>
</body>
</html>
```